依頼詳細
名刺裏面リニューアルのため、裏面のデザインをお願いいたします。
基本的にテキストのみの情報を掲載したいと思っています。
記載項目
①キャッチ
日本で唯一、新規営業に特化した営業支援会社です。

②弊社サービス紹介
・クヌーデル帳:
日本で唯一、新規営業に特化した営業ツール。
営業会社自ら、現場の声と使いやすさをもとにシステムを開発いたしました。

・企業リスト作成:
どんな営業活動も、まずはベストの営業先の見極めから。
社内、そしてWEBのデータを収集・分析を行ない、結果につながる、確度の高い企業リストを作成いたします。

・FAX集客支援:
中小企業、BtoBには非常に有効なFAXの原稿作成、またFAX配信を代行いたします。

③グループ会社一覧(社名の記載のみでかまいません)
・株式会社クレモアリス
・株式会社ミルベーナ
・ポルカノート株式会社
・株式会社ヴェルモンテ
・ハルネス株式会社
・株式会社ロザミオ
・株式会社エピフォルム
・華嶺泰股份有限公司(PELM ON RIVA CO.,LTD)
希望イメージ
シンプル 複雑
単色 カラフル
暗い 明るい
日常 高級
遊び心 厳粛
未来的 伝統的
女性的 男性的
希望する色
黒のテキストを希望します
納品ファイル
• 高解像度JPG (.jpg)
• イラストレーター形式 (.ai)
• フォトショップ形式 (.psd)
• PNG形式 (.png)
補足説明
添付にて参考までに名刺表面と既存の裏面データを送付します
当選者決定後のデータ入稿時ですが、以下の2点をお願いできますでしょうか。
------------------
①文字のアウトライン前のデータと、アウトライン済みのデータの2種類をお送
りください。
②jpg、pdfなどの見本データを一緒にお送りください。
------------------

またデザインにロゴ画像を使用していただいているご提案を当選とさせていただいた際には、
別途ロゴ画像データをお渡しいたしますので、入稿前に調整をお願いさせていただければと思います。
■ 選んだ理由

表面と並べた見たときのバランスの良さが一番のポイントとなりました。
また各コンテンツを読みやすく配置していただいており、営業の現場でもツールとして使いやすいのではないかと思ったことが選択の理由です。

■ 提案者全員のお礼・コメント

このたびは私どもの案件に多くのご提案をいただきありがとうございました。
素晴らしい提案が多く、選定に悩んでしまい、お時間をとってしまい申し訳ありませんでした。

今後もこのようなかたちでコンペを行うこともあるかと思いますが、また機会がありましたらぜひよろしくお願いいたします。

```html
<!DOCTYPE html>
<html lang="ja">
<head>
<meta charset="utf-8">
<title>名刺 裏面</title>
<link rel="stylesheet" href="https://fonts.googleapis.com/css2?family=Noto+Serif+JP:wght@400;600;700;900&family=Noto+Sans+JP:wght@500;700&display=swap">
<style>
  :root {
    --ink: #1a1a1a;
    --ink-soft: #3a3a3a;
    --accent: #3c82c8;
    --brand: #5a6f86;
    --rule: #c9c9c9;
    --frame: #d6d6d6;
    --paper: #ffffff;
    --backdrop: #f3f3f3;
  }
  * { margin: 0; padding: 0; box-sizing: border-box; }
  html, body { width: 755px; height: 1200px; overflow: hidden; background: var(--backdrop); }
  .card {
    position: absolute; left: 28px; top: 24px; width: 699px; height: 1152px;
    background: var(--paper); border: 2px solid var(--frame);
    font-family: "Noto Serif JP", serif; color: var(--ink);
    padding: 28px 34px 0;
  }
  .catch {
    border-top: 2px solid var(--ink-soft);
    border-bottom: 2px solid var(--ink-soft);
    padding: 10px 0 12px;
  }
  .catch p {
    font-weight: 900; font-size: 50px; line-height: 56px;
    text-align: justify; text-align-last: justify; letter-spacing: 0.02em;
  }
  .lead { margin-top: 18px; }
  .lead p {
    font-weight: 600; font-size: 32px; line-height: 50px;
    color: var(--ink-soft); text-align: justify; text-align-last: justify;
  }
  .lead .hl { color: var(--accent); font-weight: 700; }
  .services-title { margin-top: 22px; font-size: 19px; line-height: 26px; color: var(--ink-soft); }
  .service { margin-top: 12px; }
  .service h2 {
    font-family: "Noto Sans JP", sans-serif; font-weight: 700; font-size: 25px; line-height: 36px;
    display: flex; align-items: center; gap: 8px;
  }
  .service h2::before {
    content: ""; width: 17px; height: 17px; border-radius: 50%; background: var(--ink);
  }
  .service p {
    font-size: 20px; line-height: 34px; color: var(--ink-soft);
    padding-left: 4px;
  }
  .service + .service { margin-top: 22px; }
  .footer {
    position: absolute; left: 34px; right: 34px; bottom: 26px;
    display: flex; justify-content: space-between; align-items: flex-end;
  }
  .brand {
    display: flex; align-items: center; gap: 12px; margin-bottom: 50px;
  }
  .brand-mark { width: 38px; height: 38px; background: var(--brand); }
  .brand-name {
    font-family: "Noto Sans JP", sans-serif; font-weight: 500;
    font-size: 34px; color: var(--brand);
  }
  .group { width: 400px; }
  .group h3 { font-weight: 400; font-size: 17px; line-height: 26px; color: var(--ink-soft); margin-bottom: 4px; }
  .group ul { list-style: none; border-top: 1px solid var(--rule); padding-top: 4px; }
  .group li { font-size: 15px; line-height: 24px; color: var(--ink-soft); white-space: nowrap; }
  .group li::before { content: "・"; }
</style>
</head>
<body>
<main class="card">
  <header class="catch">
    <p>日本で唯一、</p>
    <p>新規営業に特化した</p>
    <p>営業支援会社です。</p>
  </header>

  <section class="lead">
    <p>新規営業のコストや効果のお悩みに、</p>
    <p><span class="hl">勝てる“しくみ”を収益化</span>まで</p>
    <p><span class="hl">トータルサポート</span>いたします。</p>
  </section>

  <h1 class="services-title">弊社サービスの紹介</h1>

  <section class="service">
    <h2>クヌーデル帳</h2>
    <p>日本で唯一、新規営業に特化した営業ツール。<br>営業会社自ら、現場の声と使いやすさをもとにシステムを開発いたしました。</p>
  </section>

  <section class="service">
    <h2>企業リスト作成</h2>
    <p>どんな営業活動も、まずはベストの営業先の見極めから。社内、そしてWEBのデータを収集・分析を行ない、結果につながる、確度の高い企業リストを作成いたします。</p>
  </section>

  <section class="service">
    <h2>FAX集客支援</h2>
    <p>中小企業、BtoBには非常に有効なFAXの原稿作成、またFAX配信を代行いたします。</p>
  </section>

  <footer class="footer">
    <div class="brand">
      <span class="brand-mark"></span>
      <span class="brand-name">Epiform</span>
    </div>
    <div class="group">
      <h3>グループ会社一覧</h3>
      <ul>
        <li>株式会社クレモアリス</li>
        <li>株式会社ミルベーナ</li>
        <li>ポルカノート株式会社</li>
        <li>株式会社ヴェルモンテ</li>
        <li>ハルネス株式会社</li>
        <li>株式会社ロザミオ</li>
        <li>株式会社エピフォルム</li>
        <li>華嶺泰股份有限公司（PELM ON RIVA CO.,LTD）</li>
      </ul>
    </div>
  </footer>
</main>
</body>
</html>
```